Real estate company needs a letterhead design

A young real estate company needs a letterhead / stationery design, it should include the company's logo. It should look exactly the same as on the business cards. (With the phrase "a brand of KEV Wohnbau & Grundstücksentwicklung GmbH")

In addition, it should also include the 4 round seals.

color code blue # 00456b gray # 333333

Word and PDF are welcome.

KEV Wohnbau & Grundstücksentwicklung GmbH
Managing director: Mag. Lukas Fellnhuber
Matthias-Ortner-Strasse 3c / 41
6300 Wörgl

Tel .: +436648172093
Email: office@wohnglanz-beispiel.at
Web: www.wohnglanz-beispiel.at

Sparkasse Almtal, Bergländer Sparkasse from 1882, Genossenschaftskasse
Anton-Weissauer-Strasse 7, 6300 Wörgl
IBAN: AT31 4817 2964 0058 2316
BIC: GLMTAT44XXX
Account holder: KEV Wohnbau & Grundstücksentwicklung GmbH

FN: XXXXXXX
UID: XXXXXXX

```html
<!DOCTYPE html>
<html lang="de">
<head>
<meta charset="utf-8">
<title>Wohnglanz Letterhead</title>
<link href="https://fonts.googleapis.com/css2?family=Open+Sans:ital,wght@0,400;0,600;0,700;1,600&display=swap" rel="stylesheet">
<style>
  :root {
    --brand-blue: #00456b;
    --text-gray: #333333;
    --rule: #9fb4c4;
    --divider: #dcdcdc;
    --backdrop: #e4e4e4;
    --paper: #ffffff;
    --signature-tone: #d7e3f4;
  }
  * { margin: 0; padding: 0; box-sizing: border-box; }
  html, body { width: 1200px; height: 1200px; overflow: hidden; }
  body {
    background: var(--backdrop);
    font-family: "Open Sans", Arial, sans-serif;
    color: var(--text-gray);
    display: flex; align-items: center; justify-content: center;
  }
  .letterhead {
    position: relative;
    width: 790px; height: 1118px;
    background: var(--paper);
    box-shadow: 0 6px 24px rgba(0,0,0,.12);
    padding: 64px 64px 0 64px;
  }
  .brand { display: flex; flex-direction: column; align-items: flex-start; }
  .brand-name {
    display: flex; align-items: center; gap: 8px;
    font-size: 24px; font-weight: 600; color: var(--brand-blue); line-height: 1;
  }
  .brand-mark { width: 12px; height: 12px; background: var(--brand-blue); }
  .brand-holder { font-size: 9px; color: var(--brand-blue); margin-top: 6px; }
  .letter-body { margin: 100px 0 0 92px; width: 510px; font-size: 13.5px; line-height: 1.75; }
  .recipient { margin-bottom: 26px; }
  .recipient p:nth-child(2) { padding-left: 12px; }
  .recipient p:nth-child(3) { padding-left: 24px; }
  .paragraph { text-align: justify; margin-bottom: 28px; }
  .closing { margin-top: 40px; }
  .signature { width: 220px; height: 46px; margin-top: 6px; background: var(--signature-tone); border-radius: 4px; }
  .footer {
    position: absolute; left: 64px; right: 64px; bottom: 56px;
    font-size: 10.5px; line-height: 1.6; color: var(--text-gray);
  }
  .footer strong { color: var(--brand-blue); font-weight: 700; }
  .footer-name { color: var(--brand-blue); font-weight: 600; font-style: italic; font-size: 12.5px; }
  .footer-bank { padding-bottom: 6px; border-bottom: 1px solid var(--rule); }
  .footer-row { display: flex; justify-content: space-between; padding-top: 8px; }
  .footer-col { flex: none; white-space: nowrap; padding: 0 12px; border-left: 1px solid var(--divider); }
  .footer-col:first-child { padding-left: 0; border-left: none; }
  .footer-col:last-child { padding-right: 0; }
  .footer-icon { display: inline-block; width: 10px; height: 10px; vertical-align: -1px; margin-right: 5px; }
</style>
</head>
<body>
  <main class="letterhead">
    <header class="brand">
      <div class="brand-name"><span class="brand-mark"></span>WOHNGLANZ</div>
      <p class="brand-holder">Account holder: KEV Wohnbau &amp; Grundstücksentwicklung GmbH</p>
    </header>

    <section class="letter-body">
      <div class="recipient">
        <p>To</p><p>The,</p><p>Director</p>
      </div>
      <p class="paragraph">Lorem ipsum dolor sit amet, consectetur adipiscing elit. Sed at ante. Mauris eleifend, quam a vulptate dictum, massa quam dapibus leo, eget vulputate orci purus ut lorem. In fringilla mi in ligula. Pellen tesque aliquam quam vel dolor. Nunc adipiscing. Sed quamodio, tempus ac, aliquam molestie varius ac, tellus. Vestibulum ut nulla aliquam risus rutrum interdum. Pellentesque lorem.</p>
      <p class="paragraph">Curabitur sit amet erat quis risus feugiat viverra. Pellentesque augue justo, sagittis et, lacinia at, venenatis non, arcu. Nunc nec libero. In cursus dictum risus. Etiam tristique nisl a nulla.</p>
      <p class="closing">Thanking you,</p>
      <div class="signature" role="img" aria-label="Handwritten signature of Mag. Lukas Fellnhuber"></div>
    </section>

    <footer class="footer">
      <div class="footer-bank">
        <p class="footer-name">Mag. Lukas Fellnhuber</p>
        <p>Managing director |
          <svg class="footer-icon" viewBox="0 0 10 10"><path d="M2 1l2 2-1 1.5c.6 1.2 1.3 1.9 2.5 2.5L7 6l2 2-1.5 1.5C4.5 9 1 5.5.5 2.5z" fill="#00456b"/></svg>+436648172093</p>
        <p>Sparkasse Almtal, Bergländer Sparkasse from 1882, Genossenschaftskasse, Anton-Weissauer-Strasse 7, 6300 Wörgl</p>
      </div>
      <div class="footer-row">
        <div class="footer-col">
          <p><svg class="footer-icon" viewBox="0 0 10 10"><circle cx="5" cy="5" r="4.2" fill="none" stroke="#00456b" stroke-width="1.2"/><path d="M1 5h8M5 1c-2 2.5-2 5.5 0 8M5 1c2 2.5 2 5.5 0 8" fill="none" stroke="#00456b" stroke-width=".8"/></svg>www.wohnglanz-beispiel.at</p>
          <p><svg class="footer-icon" viewBox="0 0 10 10"><rect x="0.5" y="2" width="9" height="6.5" fill="#00456b"/><path d="M.5 2l4.5 3.5L9.5 2" fill="none" stroke="#fff" stroke-width=".8"/></svg>office@wohnglanz-beispiel.at</p>
        </div>
        <div class="footer-col">
          <p><strong>BIC :</strong> GLMTAT44XXX</p>
          <p><strong>IBAN :</strong> AT31 4817 2964 0058 2316</p>
        </div>
        <div class="footer-col">
          <p><strong>FN :</strong> XXXXXXX</p>
          <p><strong>UID :</strong> XXXXXXX</p>
        </div>
        <div class="footer-col">
          <p>Matthias-Ortner-Strasse</p>
          <p>3c / 41, 6300 Wörgl</p>
        </div>
      </div>
    </footer>
  </main>
</body>
</html>
```